Zielgruppe
TECHNIKVERLEIH
EVENTMANAGEMENT
BETRIEBSSICHERHEIT
VERANSTALTUNGSSERVICE
SOLAR
Aufgabenstellung
Texte anhand der 'auftrag_o42unpfuask7_corvalin.pdf', Teaser Text für die Startseite selbst bestimmen, Farben anhand der Logos im Anhand und Ausgabe für Photoshop, XD oder PDF
Designt werden sollen die Startseite sowie eine Unterseite.

```html
<!DOCTYPE html>
<html lang="de">
<head>
<meta charset="utf-8">
<title>Corvalin – Kontakt</title>
<link href="https://fonts.googleapis.com/css2?family=Rubik:wght@400;500;700&display=swap" rel="stylesheet">
<style>
:root{
  --blue:#2a86c9;--red:#f2432c;--yellow:#fcc92f;--ink:#1f1f1f;--grey:#5e5e5e;
  --map:#e9ecf4;--panel:#f3f4f8;--line:#e6e8ee;--footer:#202020;--footer-dark:#151515;--footer-text:#b8b8b8;
}
*{margin:0;padding:0;box-sizing:border-box}
html,body{width:861px;height:1200px;overflow:hidden;background:#fff;font-family:'Rubik',sans-serif;color:var(--ink)}
.abs{position:absolute}
.header{position:absolute;left:0;top:0;width:861px;height:80px;background:#fff}
.brand{left:24px;top:30px;display:flex;align-items:center;gap:6px;font-size:17px;font-weight:500;letter-spacing:1px;color:var(--ink)}
.brand i{width:12px;height:12px;background:var(--ink);display:block}
.nav{top:33px;font-size:10.2px;color:#555;white-space:nowrap}
.nav.active{color:var(--blue);font-weight:500}
.dot{top:39px;width:2px;height:2px;border-radius:50%;background:#bbb}
.map{left:0;top:80px;width:861px;height:235px;background:var(--map)}
.form-panel{left:116px;top:370px;width:412px;height:401px;background:var(--panel)}
.info-panel{left:528px;top:370px;width:214px;height:401px;background:#fff;border:1px solid var(--line);border-bottom:none;text-align:center}
.kicker{font-size:10.5px;color:var(--red)}
.title{font-size:32px;font-weight:700;line-height:1;letter-spacing:-.2px}
.field{left:159px;width:327px;background:#fff;border-radius:19px;font-size:8.3px;color:#666;padding:0 24px;display:flex;align-items:center}
.field.area{border-radius:24px;align-items:flex-start;padding-top:23px}
.btn{left:159px;top:691px;width:120px;height:37px;background:var(--yellow);border-radius:19px;font-size:8.8px;font-weight:500;display:flex;align-items:center;justify-content:center}
.info-head{left:0;width:214px;font-size:9.5px;font-weight:500}
.info-text{left:0;width:214px;font-size:8.3px;color:var(--grey);line-height:15px}
.circle{border-radius:50%}
.footer{left:0;top:771px;width:861px;height:348px;background:var(--footer)}
.bottom{left:0;top:1119px;width:861px;height:81px;background:var(--footer-dark)}
.f-head{top:843px;font-size:13px;font-weight:500;color:#fff}
.f-text{font-size:10px;color:var(--footer-text);line-height:19px}
.f-list{left:358px;top:882px;list-style:none;font-size:10px;color:var(--footer-text)}
.f-list li{height:22.7px;display:flex;align-items:center;gap:6px}
.f-list li::before{content:"";width:2.5px;height:2.5px;border-radius:50%;background:#888}
.f-list li.current{color:#fff}
.f-list li.current::before{background:var(--red)}
.newsletter{left:63px;top:989px;width:232px;height:42px;border-radius:21px;background:#181818;font-size:10px;color:#ddd;display:flex;align-items:center;padding-left:28px}
</style>
</head>
<body>
<header class="header">
  <div class="abs brand"><i></i>CORVALIN</div>
  <span class="abs nav active" style="left:151px">Startseite</span>
  <span class="abs dot" style="left:219px"></span>
  <span class="abs nav" style="left:237px">Veranstaltungsservice</span>
  <span class="abs dot" style="left:356px"></span>
  <span class="abs nav" style="left:373px">Technikverleih</span>
  <span class="abs dot" style="left:461px"></span>
  <span class="abs nav" style="left:479px">Eventmanagement</span>
  <span class="abs dot" style="left:589px"></span>
  <span class="abs nav" style="left:607px">Betriebssicherheit</span>
  <span class="abs dot" style="left:713px"></span>
  <span class="abs nav" style="left:731px">Unternehmen</span>
</header>

<div class="abs map" role="img" aria-label="Karte mit zwei Standortmarkierungen"></div>

<section>
  <div class="abs form-panel"></div>
  <div class="abs kicker" style="left:159px;top:412px">Erzählen Sie uns von Ihrem geplanten Event</div>
  <h1 class="abs title" style="left:159px;top:428px">Nachricht schicken</h1>
  <div class="abs field" style="top:488px;height:37px">Ihr Name</div>
  <div class="abs field" style="top:535px;height:37px">Ihre E-Mail Adresse</div>
  <div class="abs field area" style="top:583px;height:97px">Was möchten Sie uns schreiben?</div>
  <div class="abs btn">Abschicken</div>

  <div class="abs info-panel">
    <div class="abs kicker" style="left:0;width:212px;top:42px">Kontakt Info</div>
    <h2 class="abs title" style="left:0;width:212px;top:58px">Details</h2>
    <div class="abs info-head" style="top:115px">Addresse</div>
    <div class="abs info-text" style="top:132px">Lindenhofweg 14<br>12459 Berlin-Uferstadt</div>
    <div class="abs info-head" style="top:179px">Telefon</div>
    <div class="abs info-text" style="top:196px">Tel.: 030/555 210 30<br>Fax: 030/555 210 31</div>
    <div class="abs info-head" style="top:243px">Email</div>
    <div class="abs info-text" style="top:260px">kontakt@corvalin-berlin.de</div>
    <div class="abs info-head" style="top:308px">Follow</div>
  </div>
  <span class="abs circle" aria-label="Soziales Netzwerk" style="left:585px;top:697px;width:32px;height:32px;background:var(--yellow)"></span>
  <span class="abs circle" aria-label="Soziales Netzwerk" style="left:621px;top:697px;width:32px;height:32px;background:var(--blue)"></span>
  <span class="abs circle" aria-label="Videokanal" style="left:658px;top:697px;width:32px;height:32px;background:var(--red)"></span>
</section>

<footer>
  <div class="abs footer"></div>
  <h3 class="abs f-head" style="left:63px">Über uns</h3>
  <h3 class="abs f-head" style="left:358px">Links</h3>
  <h3 class="abs f-head" style="left:487px">Kontakt</h3>
  <p class="abs f-text" style="left:63px;top:881px;width:255px">Die Corvalin GmbH wurde 1992, als Dienstleistungs-unternehmen für Film und Fernsehen, gegründet. Tobias Fennrich und Lukas Ambergau führen das stetig wachsende und knapp 50 Mann starke Mitarbeiterteam.</p>
  <div class="abs newsletter">Email Addresse</div>
  <div class="abs circle" style="left:256px;top:992px;width:37px;height:37px;background:var(--red)">
    <svg width="37" height="37" viewBox="0 0 37 37"><path d="M16.5 14l4.5 4.5-4.5 4.5" fill="none" stroke="#fff" stroke-width="1.6" stroke-linecap="round" stroke-linejoin="round"/></svg>
  </div>
  <ul class="abs f-list">
    <li>Impressum</li>
    <li class="current">Kontakt</li>
    <li>Datenschutz</li>
    <li>Cookies</li>
  </ul>
  <div class="abs f-text" style="left:487px;top:881px">030/555 210 30</div>
  <div class="abs f-text" style="left:487px;top:911px">kontakt@corvalin-berlin.de</div>
  <div class="abs f-text" style="left:487px;top:941px;line-height:15px">Lindenhofweg 14<br>12459 Berlin-Uferstadt</div>
  <div class="abs bottom"></div>
  <div class="abs f-text" style="left:63px;top:1150px">© Copyright 2022 Corvalin GmbH</div>
  <span class="abs circle" aria-label="Soziales Netzwerk" style="left:676px;top:1141px;width:37px;height:37px;background:var(--yellow)"></span>
  <span class="abs circle" aria-label="Soziales Netzwerk" style="left:719px;top:1141px;width:37px;height:37px;background:var(--blue)"></span>
  <span class="abs circle" aria-label="Videokanal" style="left:762px;top:1141px;width:37px;height:37px;background:var(--red)"></span>
</footer>
</body>
</html>
```